Flyer creation for holiday food gift programs

1. Flyer Background (sample of last years flyer is attached)a. Purpose – to promote holiday food gift businessb. Where is it used - We feature this flyer on our website for our customer (distributors) to download print and or email to their clients.c. Customers (distributors) have the option to put their logo and contact info on the bottom portion of the flyer, (as to why the bottom 2.5 inches is empty/or faded).d. Our customers (distributors) use this flyer to market to their clients (end-buyers) how food gifts.1. They email or print it off and hand it out.2. They send it to current end-buyers and new end-buyerse. I have attached 6 images to use without their background,, please use the three that best fit your layout. I was only able to upload jpgs. I can send the hi res when you know which one you want to use.1. Item# KM415 from $39 to $662. Item#FSJ863 from $14 to $243. Item#VMA5824 from $44 to $674. Item#PLO6142 from $69 to $2495. Item#ZES758 from $24 to $496. Item#N4836 from $62 to $99f. The call to action is to get the end-buyer to contact the customer (distributor)g. The below can also be used in bullets, the first being a headline.1. Achieve the most from your business gifting! or Make Gift-Giving Unforgettable!2. Your logo on every gift3. Stress free gift giving4. Delicious Gifts they’ll remember and enjoy.5. Your one stop shop6. Gifts to fit every price pointh. If you have any questions, please feel free to email us. You can view our website for a better feel of our products and you can also view our white paper to understand our background, see attached.

Target Market(s)

Corporations that purchase holiday gifts for their employees and customers.

Requirements
Nice to have
• Elegant design and a holiday look
Should not have
• Green usually doesn't work well with food. No Christmas trees.

```html
<!DOCTYPE html>
<html lang="en">
<head>
<meta charset="utf-8">
<title>Business Gifting Flyer</title>
<link href="https://fonts.googleapis.com/css2?family=Oswald:wght@400;500;600;700&family=Montserrat:wght@600;700&family=Allura&display=swap" rel="stylesheet">
<style>
  :root {
    --wine: #7d1a22;
    --orange: #e8902a;
    --gold-text: #f4b860;
    --beige: #e2d6c7;
    --linen: #ecedee;
    --sage: #93a886;
    --sage-dark: #4a6a3e;
    --lilac: #a08aa9;
    --lilac-dark: #5e3f62;
    --tan: #b08b6c;
    --tan-dark: #6e3d22;
    --ink: #1e1e1e;
  }
  * { margin: 0; padding: 0; box-sizing: border-box; }
  html, body { width: 888px; height: 1200px; overflow: hidden; }
  body { background: #fff; }
  .flyer {
    position: relative; width: 888px; height: 1200px; overflow: hidden;
    background: linear-gradient(180deg, #f1f1f2 0%, var(--linen) 60%, #e6e7e8 100%);
    font-family: "Oswald", sans-serif;
  }
  .backdrop { position: absolute; inset: 0; }
  .headline {
    position: absolute; right: 18px; top: 40px; text-align: right; color: var(--wine);
    text-transform: uppercase; font-family: "Oswald", sans-serif; line-height: 1;
  }
  .headline .kicker { font-size: 33px; font-weight: 500; letter-spacing: 0.2px; }
  .headline .main { font-size: 66px; font-weight: 600; margin-top: 6px; letter-spacing: 0.5px; }

  .product-card {
    position: absolute; width: 322px; height: 399px; transform: rotate(-6deg);
    box-shadow: 0 2px 6px rgba(0,0,0,0.12);
  }
  .product-card .frame {
    position: absolute; left: 20px; top: 20px; width: 284px; height: 272px;
    background: #fff; border: 5px solid; padding: 8px;
  }
  .product-card .photo { width: 100%; height: 100%; }
  .product-card .name {
    position: absolute; left: 0; right: 16px; top: 314px; text-align: right;
    font-family: "Montserrat", sans-serif; font-weight: 700; font-size: 19px; color: #fff; letter-spacing: 0.3px;
  }
  .product-card .price {
    position: absolute; left: 0; right: 20px; top: 338px; text-align: right;
    font-family: "Allura", cursive; font-size: 36px; color: #fff;
  }
  .card-chocolate { left: 107px; top: 312px; background: var(--sage); }
  .card-chocolate .frame { border-color: var(--sage-dark); }
  .card-chocolate .photo { background: radial-gradient(ellipse at 50% 55%, #8a5a3a 0%, #c9a882 35%, #fff 70%); }
  .card-tower { left: 506px; top: 187px; background: var(--lilac); }
  .card-tower .frame { border-color: var(--lilac-dark); }
  .card-tower .photo { background: radial-gradient(ellipse at 50% 50%, #2a2f55 0%, #b99a62 40%, #fff 72%); }
  .card-cheese { left: 503px; top: 620px; background: var(--tan); }
  .card-cheese .frame { border-color: var(--tan-dark); }
  .card-cheese .photo { background: radial-gradient(ellipse at 50% 55%, #2b2b2b 0%, #e8b93f 35%, #fff 70%); }
  .card-cheese .price { color: var(--tan-dark); }

  .benefits { position: absolute; left: 31px; top: 751px; list-style: none; }
  .benefits li {
    height: 32px; margin-bottom: 11px; background: var(--wine);
    border-left: 4px solid var(--orange); color: var(--gold-text);
    font-size: 18px; font-weight: 500; line-height: 32px; padding-left: 17px;
    clip-path: polygon(0 0, calc(100% - 24px) 0, 100% 100%, 0 100%);
  }
  .footer-band {
    position: absolute; left: 0; right: 0; top: 1044px; height: 129px;
    background: linear-gradient(90deg, rgba(210,190,172,0) 35%, rgba(200,178,158,0.75) 100%);
  }
  .distributor { position: absolute; left: 40px; width: 457px; top: 1052px; text-align: center; color: var(--ink); }
  .distributor .label { font-size: 18px; font-weight: 600; }
  .distributor .logo-name { font-size: 42px; font-weight: 700; line-height: 1.05; }
  .distributor .rule { height: 1px; background: var(--ink); margin-top: 6px; }
  .distributor .address { font-size: 15px; font-weight: 400; margin-top: 6px; }
  .contact { position: absolute; left: 567px; top: 1064px; color: var(--ink); font-size: 17px; line-height: 34px; }
  .contact .lead { font-weight: 600; font-size: 18px; }
  .contact strong { font-weight: 600; font-size: 23px; }
</style>
</head>
<body>
<div class="flyer">
  <svg class="backdrop" width="888" height="1200" viewBox="0 0 888 1200" aria-hidden="true">
    <defs>
      <linearGradient id="handsGrad" x1="0" y1="0" x2="1" y2="1">
        <stop offset="0" stop-color="#e9c9b4"/>
        <stop offset="0.45" stop-color="#d9a17f"/>
        <stop offset="0.7" stop-color="#c9a04a"/>
        <stop offset="1" stop-color="#efe7df"/>
      </linearGradient>
      <linearGradient id="handsFade" x1="0" y1="0" x2="1" y2="0">
        <stop offset="0.75" stop-color="#e2d6c7" stop-opacity="0"/>
        <stop offset="1" stop-color="#e2d6c7" stop-opacity="1"/>
      </linearGradient>
      <clipPath id="topArea">
        <path d="M0,0 H888 V218 C700,215 560,225 480,236 C330,262 160,340 0,452 Z"/>
      </clipPath>
    </defs>
    <path d="M0,0 H888 V218 C700,215 560,225 480,236 C330,262 160,340 0,452 Z" fill="var(--beige)"/>
    <g clip-path="url(#topArea)">
      <rect x="0" y="0" width="516" height="360" fill="url(#handsGrad)" role="img" aria-label="Photo of hands offering a gold gift box tied with a red ribbon"/>
      <rect x="0" y="0" width="516" height="360" fill="url(#handsFade)"/>
    </g>
    <path d="M0,452 C160,340 330,262 480,236 C560,225 700,215 888,218 V227 C700,225 560,236 486,248 C340,274 170,354 0,482 Z" fill="var(--wine)"/>
    <path d="M0,492 C172,362 342,280 488,255 C562,242 700,232 888,233" fill="none" stroke="var(--orange)" stroke-width="3"/>
  </svg>

  <header class="headline">
    <div class="kicker">Achieve the most from your</div>
    <div class="main">Business Gifting!</div>
  </header>

  <article class="product-card card-tower">
    <div class="frame"><div class="photo" role="img" aria-label="Product photo of a gourmet gift tower with navy and gold boxes, popcorn, chocolates and cookies"></div></div>
    <div class="name">Gourmet Gift Tower</div>
    <div class="price">from $69 to $249</div>
  </article>

  <article class="product-card card-chocolate">
    <div class="frame"><div class="photo" role="img" aria-label="Product photo of a gourmet chocolate tower with wooden crates of chocolate treats"></div></div>
    <div class="name">Gourmet Chocolate Tower</div>
    <div class="price">from $44 to $67</div>
  </article>

  <article class="product-card card-cheese">
    <div class="frame"><div class="photo" role="img" aria-label="Product photo of a slate serving board with cheeses, sausage and crackers"></div></div>
    <div class="name">Gourmet Gift Tower</div>
    <div class="price">from $62 to $99</div>
  </article>

  <ul class="benefits">
    <li style="width:290px">Your logo on every gift</li>
    <li style="width:260px">Stress free gift giving</li>
    <li style="width:443px">Delicious Gifts they’ll remember and enjoy.</li>
    <li style="width:238px">Your one stop shop</li>
    <li style="width:316px">Gifts to fit every price point</li>
  </ul>

  <div class="footer-band"></div>
  <div class="distributor">
    <div class="label">Distributor’s</div>
    <div class="logo-name">LOGO</div>
    <div class="rule"></div>
    <div class="address">&amp; Address line will be here</div>
  </div>
  <div class="contact">
    <div class="lead">To know about other products :</div>
    <div>Call us Today <strong>+000 000 000</strong></div>
    <div>or Mail : <strong>hello@tidingsbox.com</strong></div>
  </div>
</div>
</body>
</html>
```